Get Up to $ 500,000 in Business Capital within 48 hours

design a flyer offering business capital to businesses. The flyer is going to be mailed to business owners and the flyer needs to immediately capture their attention.
The flyer needs to be bold and professional and really stand-out.
pppppppppppppppppppppppppppppppppppppppppppppppppppppppppppppppppppppppppppppppppppppppppppppppppppppppppppppppppppppppppppppppppppppppppppppppppppppppppppppppppppppppppppppppppppppppppppppppppppppppppppppppppppppppppppppppppppppp

Target Market(s)

business owners

Font styles to use
Serif

Requirements
Must have
• Apply online in minutes at PellarCapital.example or call 800-GRAB-NOW
Nice to have
• We fund almost every business type. Not a business loan, receive a cash advance on your future sales.

```html
<!DOCTYPE html>
<html lang="en">
<head>
<meta charset="utf-8">
<title>Pellar Capital – Business Capital Flyer</title>
<link href="https://fonts.googleapis.com/css2?family=Roboto+Condensed:wght@300;400;700;800&family=Montserrat:wght@500;600&display=swap" rel="stylesheet">
<style>
  :root{
    --page:#ffffff;
    --ink:#232323;
    --brand-blue:#2a88cc;
    --logo-blue:#1f6fc0;
    --panel-teal:#0a76a6;
    --panel-blue:#1560b8;
    --white:#ffffff;
    --photo-light:#eef2f4;
    --photo-mid:#c9dadf;
    --photo-suit:#2c3553;
  }
  *{margin:0;padding:0;box-sizing:border-box}
  html,body{width:1200px;height:1200px;overflow:hidden;background:var(--page)}
  .flyer{position:absolute;left:233px;top:124px;width:741px;height:960px;overflow:hidden;background:var(--photo-light)}
  .hero-photo{position:absolute;inset:0;
    background:
      radial-gradient(ellipse 150px 330px at 490px 400px, rgba(44,53,83,.85), rgba(44,53,83,0) 100%),
      linear-gradient(100deg, #f3f5f7 0%, #e6eef1 40%, var(--photo-mid) 100%);}
  .logo{position:absolute;left:36px;top:52px;font-family:'Roboto Condensed',sans-serif;font-weight:700;font-size:52px;line-height:1;color:var(--logo-blue);letter-spacing:-.5px}
  .headline{position:absolute;left:36px;font-family:'Roboto Condensed',sans-serif;font-weight:800;font-size:74px;line-height:1;letter-spacing:-1px;color:var(--ink)}
  .headline.need{top:170px;color:var(--brand-blue)}
  .headline.business{top:243px}
  .headline.capital{top:319px}
  .rule-dark{position:absolute;left:36px;top:398px;width:120px;height:3px;background:var(--ink)}
  .panel{position:absolute;inset:0;width:741px;height:960px}
  .offer{position:absolute;left:36px;font-family:'Roboto Condensed',sans-serif;color:var(--white);line-height:1}
  .offer.light{font-weight:300;font-size:52px}
  .offer.you{top:518px}
  .offer.qualify{top:568px}
  .offer.amount{top:622px;font-weight:700;font-size:50px}
  .offer.hours{top:671px;font-weight:700;font-size:38px}
  .rule-light{position:absolute;left:36px;top:723px;width:270px;height:2px;background:var(--white)}
  .perk{position:absolute;left:36px;display:flex;align-items:center;gap:11px;font-family:'Montserrat',sans-serif;font-weight:600;font-size:20px;color:var(--white)}
  .perk svg{width:28px;height:28px}
  .perk.credit{top:748px}
  .perk.application{top:809px}
  .benefit{position:absolute;left:435px;display:flex;align-items:center;gap:19px;font-family:'Montserrat',sans-serif;font-weight:600;font-size:16px;line-height:22px;color:var(--white)}
  .benefit svg{width:48px;height:48px;flex:none}
  .benefit.advance{top:607px}
  .benefit.alternative{top:704px}
  .benefit.every{top:779px}
  .cta{position:absolute;left:36px;top:878px;width:669px;height:35px;border:1.5px solid var(--white);display:flex;align-items:center;justify-content:center;font-family:'Montserrat',sans-serif;font-weight:600;font-size:16.5px;color:var(--white);letter-spacing:.2px}
</style>
</head>
<body>
<main class="flyer">
  <div class="hero-photo" role="img" aria-label="Photo of a smiling businessman in a pinstripe suit holding a laptop in a bright office"></div>

  <div class="logo">PELLARCAPITAL</div>

  <h1>
    <span class="headline need">NEED</span>
    <span class="headline business">BUSINESS</span>
    <span class="headline capital">CAPITAL?</span>
  </h1>
  <div class="rule-dark"></div>

  <svg class="panel" viewBox="0 0 741 960" aria-hidden="true">
    <defs>
      <linearGradient id="panelFill" x1="0" y1="0" x2="1" y2="1">
        <stop offset="0" stop-color="#0a76a6"/>
        <stop offset="1" stop-color="#1560b8"/>
      </linearGradient>
      <linearGradient id="panelRight" x1="0" y1="0" x2="1" y2="1">
        <stop offset="0" stop-color="#1456b6"/>
        <stop offset="1" stop-color="#0d6fb5"/>
      </linearGradient>
    </defs>
    <polygon points="0,419 343,501 366,595 741,521 741,960 0,960" fill="url(#panelFill)"/>
    <polygon points="366,595 741,521 741,960 420,960" fill="url(#panelRight)" opacity=".55"/>
  </svg>

  <p class="offer light you">YOU CAN</p>
  <p class="offer light qualify">QUALIFY FOR</p>
  <p class="offer amount">UP TO 500,000</p>
  <p class="offer hours">IN JUST 24 HOURS</p>
  <div class="rule-light"></div>

  <div class="perk credit">
    <svg viewBox="0 0 28 28" fill="none" stroke="#fff" stroke-width="1.4"><path d="M2 12 14 4l12 8v12H2z"/><path d="M2 12l12 8 12-8"/><rect x="6" y="7" width="16" height="9" fill="#0a76a6"/><circle cx="22" cy="22" r="4" fill="#0a76a6"/></svg>
    <span>No minimum credit score</span>
  </div>
  <div class="perk application">
    <svg viewBox="0 0 28 28" fill="none" stroke="#fff" stroke-width="1.4"><rect x="5" y="2" width="18" height="24"/><rect x="8" y="5" width="5" height="5"/><path d="M15 6h5M15 9h5M8 14l1.5 1.5L12 13M14 14h6M8 19l1.5 1.5L12 18M14 19h6"/></svg>
    <span>Simple 1 page application</span>
  </div>

  <div class="benefit advance">
    <svg viewBox="0 0 48 48" fill="none" stroke="#fff" stroke-width="1.5"><circle cx="24" cy="24" r="23"/><rect x="13" y="22" width="22" height="11"/><circle cx="24" cy="27.5" r="3"/><path d="M15 19h6v3M23 16h5v6M31 14l2-3 2 3M33 11v8"/></svg>
    <span>Not a business loan,<br>get a cash advance today<br>on your future sales</span>
  </div>
  <div class="benefit alternative">
    <svg viewBox="0 0 48 48" fill="none" stroke="#fff" stroke-width="1.5"><circle cx="24" cy="24" r="23"/><rect x="13" y="12" width="18" height="24"/><path d="M16 17h12M16 22h8M16 26h8M16 30h6M29 32l7-12"/></svg>
    <span>Convenient alternative to<br>a bank loan</span>
  </div>
  <div class="benefit every">
    <svg viewBox="0 0 48 48" fill="none" stroke="#fff" stroke-width="1.5"><circle cx="24" cy="24" r="23"/><rect x="12" y="22" width="18" height="11"/><path d="M15 19v-4M19 19v-6M23 19v-3M27 19v-5"/><circle cx="32" cy="30" r="5"/></svg>
    <span>We fund virtually every<br>type of business</span>
  </div>

  <div class="cta">Apply in minutes online at PellarCapital.example or call 1-800-GRAB-NOW</div>
</main>
</body>
</html>
```